Ashcombe Field Surveyors Business Card

We are a land surveying company looking for a business card with a clean, sharp design. We would like for our design to portray our logo on one side, and contact information on the other w/ or w/o logo. Our colors preferred are navy blue, grey/silver, white and black. thank you!

Industry/Entity Type

Surveyor

Contact Information for Business Card

Ashcombe Field Surveyors
Dorian Kavatsky, P.L.S.
(555) 302-4619
Ashcombefieldsurveyors@ashmail-example.net
Ashcombefieldsurveyors-example.com
287 Linden Terrace, Millbrook VT 05999

Requirements
Must have
• 1. Company Name
2. Personal name and title
3. phone number
4. email.
5. website
6. address

```html
<!DOCTYPE html>
<html lang="en">
<head>
<meta charset="utf-8">
<title>Ashcombe Field Surveyors – Business Card</title>
<link href="https://fonts.googleapis.com/css2?family=Roboto:ital,wght@0,400;0,500;1,700&display=swap" rel="stylesheet">
<style>
  :root {
    --backdrop: #2a2a2c;
    --card: #1c1c1e;
    --navy: #2f3aa8;
    --silver: #b9bcc2;
    --white: #f2f2f2;
  }
  * { box-sizing: border-box; margin: 0; padding: 0; }
  html, body {
    width: 1200px; height: 900px; overflow: hidden;
    background: var(--backdrop);
    font-family: "Roboto", sans-serif;
  }
  .sheet { position: relative; width: 1200px; height: 900px; }
  .card {
    position: absolute; left: 250px; width: 700px; height: 400px;
    background: var(--card);
    border-radius: 4px;
    box-shadow: 0 12px 30px rgba(0,0,0,.45);
    overflow: hidden;
  }
  .card--front { top: 35px; }
  .card--back { top: 465px; }

  .front-name {
    position: absolute; right: 60px; bottom: 70px;
    display: flex; align-items: center; gap: 18px;
  }
  .front-name__mark {
    width: 44px; height: 44px; border: 3px solid var(--silver); border-radius: 50%;
  }
  .front-name__text {
    font-weight: 500; font-size: 34px; letter-spacing: 3px;
    color: var(--navy); text-transform: uppercase; line-height: 1.15;
  }

  .back-brand {
    position: absolute; left: 50px; top: 150px; width: 240px;
    display: flex; align-items: center; gap: 12px;
  }
  .back-brand__mark {
    flex: none; width: 28px; height: 28px; border: 2px solid var(--silver); border-radius: 50%;
  }
  .back-brand__text {
    font-weight: 500; font-size: 20px; letter-spacing: 2px;
    color: var(--navy); text-transform: uppercase; line-height: 1.2;
  }
  .divider {
    position: absolute; left: 310px; top: 70px; width: 2px; height: 260px;
    background: var(--navy);
  }
  .contact {
    position: absolute; left: 335px; top: 95px; right: 20px;
    color: var(--white); font-size: 15px; line-height: 23px;
  }
  .contact__name {
    font-style: italic; font-weight: 700; font-size: 21px;
    color: var(--navy); margin-bottom: 4px;
  }
  .contact__line { display: flex; align-items: center; gap: 8px; white-space: nowrap; }
  .contact__icon { width: 13px; height: 13px; flex: none; }
</style>
</head>
<body>
<main class="sheet">
  <section class="card card--front" aria-label="Card front">
    <div class="front-name">
      <span class="front-name__mark"></span>
      <span class="front-name__text">Ashcombe<br>Field Surveyors</span>
    </div>
  </section>

  <section class="card card--back" aria-label="Card back">
    <div class="back-brand">
      <span class="back-brand__mark"></span>
      <span class="back-brand__text">Ashcombe Field Surveyors</span>
    </div>
    <div class="divider"></div>
    <div class="contact">
      <p class="contact__name">Dorian Kavatsky, P.L.S.</p>
      <p class="contact__line">Ashcombe Field Surveyors</p>
      <p class="contact__line">287 Linden Terrace</p>
      <p class="contact__line">Millbrook VT 05999</p>
      <p class="contact__line">
        <svg class="contact__icon" viewBox="0 0 16 16"><path fill="var(--navy)" d="M3 1l3 3-2 2c1 2 3 4 5 5l2-2 3 3-2 2C6 14 2 10 1 3z"/></svg>
        (555) 302-4619
      </p>
      <p class="contact__line">
        <svg class="contact__icon" viewBox="0 0 16 16"><rect x="1" y="3" width="14" height="10" fill="var(--navy)"/><path d="M1 3l7 6 7-6" stroke="var(--card)" stroke-width="1.4" fill="none"/></svg>
        Ashcombefieldsurveyors@ashmail-example.net
      </p>
      <p class="contact__line">
        <svg class="contact__icon" viewBox="0 0 16 16"><circle cx="8" cy="8" r="7" fill="var(--navy)"/><path d="M1 8h14M8 1c-3 4-3 10 0 14M8 1c3 4 3 10 0 14" stroke="var(--card)" stroke-width="1" fill="none"/></svg>
        Ashcombefieldsurveyors-example.com
      </p>
    </div>
  </section>
</main>
</body>
</html>
```